UI Improvement for FlorQuay app

We are looking for a talented UI/UX designer to REFINE and enhance the visual design of our mobile application, FlorQuay. The app is fully functional, but we need a designer to improve its aesthetics by specifying design elements such as fonts, colors, spacing, and component styles.
Your task will be to analyze the CURRENT UI and provide detailed design specifications that will make the app more visually appealing, modern, and user-friendly.
TODO:
Review the existing FlorQuay app design (see attachments) and identify areas for visual improvement.
Provide a detailed UI style guide, including:
Typography (font choices, sizes, and weights)
Color palette (primary, secondary, and accent colors)
Component styling (buttons, forms, icons, and interactive elements)
Spacing and layout guidelines (margins, paddings, and alignment)
Ensure the design remains clean, modern, and professional while maintaining usability and accessibility.
Provide design mockups or visual examples (if possible) to illustrate the proposed changes.
Deliverables:
A UI Style Guide (PDF or Figma file) with specifications on fonts, colors, spacing, and UI components.
Optionally, before/after mockups or examples demonstrating the improvements.
Ideal Designer:
Strong experience in mobile UI/UX design.
Understanding of modern design trends and best practices.
Ability to communicate design choices clearly for easy developer implementation.
I have attached 7 images showcasing the main UI screens used in the FlorQuay app. These screens need visual enhancements to improve their overall look and user experience.
The images represent the current design in three key modes:
LIST Mode – Displays data in a structured list format.
READ Mode – Shows detailed information when a user selects an item.
ADD/EDIT Mode – Allows users to input or modify information.
Additionally, there is a ‘MORE’ page, which serves as a menu listing other features of the application.
Task Objective:
Please refine and improve these UIs to create a more modern, visually appealing, and user-friendly experience. Focus on typography, colors, spacing, and component styling to ensure a cohesive and polished design.
Look and feel
Each slider illustrates characteristics of the customer's brand and the style your logo design should communicate.

```html
<!DOCTYPE html>
<html lang="en">
<head>
<meta charset="utf-8">
<title>FlorQuay – Contact Screens</title>
<link href="https://fonts.googleapis.com/css2?family=Inter:wght@400;500;600;700&display=swap" rel="stylesheet">
<style>
:root{
  --page:#e9ebef;
  --screen:#f4f4f4;
  --surface:#ffffff;
  --ink:#111111;
  --ink-soft:#333333;
  --muted:#8a8a8a;
  --line:#d9d9d9;
  --brand:#0b57b0;
  --accent:#3aa877;
  --tag-bg:#d6e9fb;
  --tag-ink:#1b5aa6;
  --avatar:#f6e4f5;
}
*{box-sizing:border-box;margin:0;padding:0}
html,body{width:1200px;height:933px;overflow:hidden;background:var(--page);font-family:"Inter",sans-serif;color:var(--ink)}
.stage{position:absolute;left:0;top:0;width:1600px;height:1244px;transform:scale(.75);transform-origin:0 0}
.screen{position:absolute;top:195px;width:390px;height:850px;background:var(--screen);border-radius:44px;overflow:hidden;box-shadow:0 10px 30px rgba(0,0,0,.08)}
.screen--list{left:114px}
.screen--form{left:605px}
.screen--detail{left:1096px}
.abs{position:absolute}
.status-time{left:22px;top:18px;font-size:15px;font-weight:600}
.island{left:133px;top:16px;width:123px;height:36px;border-radius:18px;background:#111}
.status-icons{right:24px;top:20px}
.title{left:0;right:0;top:76px;text-align:center;font-size:24px;font-weight:700}
.add-btn{left:335px;top:74px;width:32px;height:32px;border-radius:50%;background:var(--accent)}
.search{left:22px;top:130px;width:345px;height:48px;border:1px solid #9a9a9a;border-radius:4px;background:var(--surface);display:flex;align-items:center;gap:10px;padding-left:16px;font-size:16px;color:var(--muted)}
.tabs{left:22px;top:221px;display:flex;gap:16px;font-size:14px;color:#a3a3a3}
.tab--active{color:var(--brand);font-weight:600;position:relative}
.tab--active::after{content:"";position:absolute;left:-3px;right:-3px;bottom:-9px;height:2px;background:var(--brand)}
.contact-card{left:22px;width:345px;height:80px;background:var(--surface);border-radius:4px}
.avatar{left:8px;top:8px;width:64px;height:64px;background:var(--avatar);border-radius:2px;display:flex;align-items:center;justify-content:center;font-size:30px;font-weight:500}
.contact-name{left:87px;top:15px;font-size:16px;font-weight:500}
.tags{left:87px;top:45px;display:flex;gap:6px}
.tag{background:var(--tag-bg);color:var(--tag-ink);font-size:8px;font-weight:500;height:17px;line-height:17px;padding:0 11px;border-radius:9px}
.tabbar{left:0;bottom:0;width:100%;height:80px;background:var(--surface);border-top:1px solid #ececec;display:flex;justify-content:space-around;padding:18px 14px 0}
.tab-item{display:flex;flex-direction:column;align-items:center;gap:4px;font-size:8px;color:var(--ink-soft);width:60px}
.tab-item--active{color:var(--brand)}
.home-bar{left:133px;bottom:5px;width:123px;height:4px;border-radius:2px;background:#111}
.nav-link{top:83px;font-size:14px}
.nav-cancel{left:22px;color:#777}
.nav-save{right:22px;color:var(--accent)}
.field-label{left:22px;font-size:12px;font-weight:600}
.field{left:22px;width:345px;height:48px;background:var(--surface);border:1px solid #e2e2e2;border-radius:2px;font-size:14px;color:#7a7a7a;padding:14px 15px}
.divider{left:0;top:511px;width:100%;height:1px;background:#e2e2e2}
.back{left:24px;top:82px}
.row{left:22px;width:345px;height:56px;background:var(--surface);display:flex;align-items:center;justify-content:space-between;padding:0 24px 0 16px;font-size:16px;font-weight:500;color:var(--ink-soft)}
.group{left:22px;top:576px;width:345px;height:131px;background:var(--surface);padding:0 22px 0 16px}
.group-head{display:flex;justify-content:space-between;align-items:center;height:56px;font-size:16px;font-weight:600;color:var(--ink-soft)}
.group-line{font-size:14px;color:#555;border-bottom:1px solid var(--line);padding-bottom:2px;margin-bottom:13px}
.group-line b{font-weight:500;color:var(--ink-soft);margin-right:8px}
</style>
</head>
<body>
<div class="stage">

  <!-- Contacts list -->
  <section class="screen screen--list">
    <div class="abs status-time">9:41</div>
    <div class="abs island"></div>
    <svg class="abs status-icons" width="62" height="12" viewBox="0 0 62 12"><rect x="0" y="8" width="3" height="4" fill="#111"/><rect x="4" y="6" width="3" height="6" fill="#111"/><rect x="8" y="4" width="3" height="8" fill="#111"/><rect x="12" y="1" width="3" height="11" fill="#111"/><path d="M22 5a9 9 0 0 1 12 0M24.5 7.5a5 5 0 0 1 7 0" stroke="#111" stroke-width="1.8" fill="none"/><circle cx="28" cy="10.5" r="1.4" fill="#111"/><rect x="39" y="1" width="21" height="10" rx="3" fill="none" stroke="#111"/><rect x="41" y="3" width="17" height="6" rx="1.5" fill="#111"/></svg>
    <h1 class="abs title">Contacts</h1>
    <div class="abs add-btn"><svg width="32" height="32" viewBox="0 0 32 32"><path d="M16 10v12M10 16h12" stroke="#fff" stroke-width="2" stroke-linecap="round"/></svg></div>
    <div class="abs search"><svg width="20" height="20" viewBox="0 0 20 20"><circle cx="9" cy="9" r="6.5" stroke="#333" stroke-width="1.6" fill="none"/><path d="M14 14l4 4" stroke="#333" stroke-width="1.6" stroke-linecap="round"/></svg>Search</div>
    <nav class="abs tabs"><span class="tab--active">Pilot</span><span>Owner</span><span>Plane</span><span>Aircraft Owner</span><span>Supplier</span></nav>

    <div class="abs contact-card" style="top:271px"><div class="abs avatar">A</div><div class="abs contact-name">Brennan,Lowell</div><div class="abs tags"><span class="tag">Aircraft Owner</span><span class="tag">Pilot</span><span class="tag">Flight Suplier</span></div></div>
    <div class="abs contact-card" style="top:355px"><div class="abs avatar">A</div><div class="abs contact-name">Brennan,Lowell</div><div class="abs tags"><span class="tag">Aircraft Owner</span><span class="tag">Pilot</span><span class="tag">Flight Suplier</span></div></div>
    <div class="abs contact-card" style="top:439px"><div class="abs avatar">A</div><div class="abs contact-name">Brennan,Lowell</div><div class="abs tags"><span class="tag">Aircraft Owner</span><span class="tag">Pilot</span><span class="tag">Flight Suplier</span></div></div>
    <div class="abs contact-card" style="top:523px"><div class="abs avatar">A</div><div class="abs contact-name">Brennan,Lowell</div><div class="abs tags"><span class="tag">Aircraft Owner</span><span class="tag">Pilot</span><span class="tag">Flight Suplier</span></div></div>
    <div class="abs contact-card" style="top:607px"><div class="abs avatar">A</div><div class="abs contact-name">Brennan,Lowell</div><div class="abs tags"><span class="tag">Aircraft Owner</span><span class="tag">Pilot</span><span class="tag">Flight Suplier</span></div></div>
    <div class="abs contact-card" style="top:691px"><div class="abs avatar">A</div><div class="abs contact-name">Brennan,Lowell</div><div class="abs tags"><span class="tag">Aircraft Owner</span><span class="tag">Pilot</span><span class="tag">Flight Suplier</span></div></div>

    <nav class="abs tabbar">
      <div class="tab-item tab-item--active"><svg width="22" height="22" viewBox="0 0 22 22" fill="none" stroke="currentColor" stroke-width="1.6"><circle cx="11" cy="7" r="3.5"/><path d="M4 19c0-4 3-6 7-6s7 2 7 6z" stroke-linejoin="round"/></svg>Contact</div>
      <div class="tab-item"><svg width="22" height="22" viewBox="0 0 22 22" fill="none" stroke="currentColor" stroke-width="1.6" stroke-linejoin="round"><path d="M11 3l7 4v8l-7 4-7-4V7z M4 7l7 4 7-4 M11 11v8"/></svg>Quote</div>
      <div class="tab-item"><svg width="22" height="22" viewBox="0 0 22 22" fill="none" stroke="currentColor" stroke-width="1.6"><rect x="3" y="7" width="16" height="12" rx="1.5"/><path d="M8 7V4h6v3M8 7v12M14 7v12"/></svg>Work Order</div>
      <div class="tab-item"><svg width="22" height="22" viewBox="0 0 22 22" fill="none" stroke="currentColor" stroke-width="1.6"><rect x="5" y="4" width="12" height="16" rx="1.5"/><rect x="8" y="2.5" width="6" height="3" rx="1"/></svg>Invoice</div>
      <div class="tab-item"><svg width="22" height="22" viewBox="0 0 22 22" fill="currentColor"><circle cx="5" cy="11" r="1.6"/><circle cx="11" cy="11" r="1.6"/><circle cx="17" cy="11" r="1.6"/></svg>More</div>
    </nav>
    <div class="abs home-bar"></div>
  </section>

  <!-- Add contact form -->
  <section class="screen screen--form">
    <div class="abs status-time">9:41</div>
    <div class="abs island"></div>
    <svg class="abs status-icons" width="62" height="12" viewBox="0 0 62 12"><rect x="0" y="8" width="3" height="4" fill="#111"/><rect x="4" y="6" width="3" height="6" fill="#111"/><rect x="8" y="4" width="3" height="8" fill="#111"/><rect x="12" y="1" width="3" height="11" fill="#111"/><path d="M22 5a9 9 0 0 1 12 0M24.5 7.5a5 5 0 0 1 7 0" stroke="#111" stroke-width="1.8" fill="none"/><circle cx="28" cy="10.5" r="1.4" fill="#111"/><rect x="39" y="1" width="21" height="10" rx="3" fill="none" stroke="#111"/><rect x="41" y="3" width="17" height="6" rx="1.5" fill="#111"/></svg>
    <span class="abs nav-link nav-cancel">Cancel</span>
    <h1 class="abs title">Add Contact</h1>
    <span class="abs nav-link nav-save">Save</span>

    <label class="abs field-label" style="top:149px">Business name</label>
    <div class="abs field" style="top:171px">Company name</div>
    <label class="abs field-label" style="top:236px">First name</label>
    <div class="abs field" style="top:258px">Company name</div>
    <label class="abs field-label" style="top:323px">Middle name</label>
    <div class="abs field" style="top:345px">Company name</div>
    <label class="abs field-label" style="top:410px">Last name</label>
    <div class="abs field" style="top:432px">Company name</div>

    <div class="abs divider"></div>

    <label class="abs field-label" style="top:545px">Address</label>
    <div class="abs field" style="top:567px"></div>
    <label class="abs field-label" style="top:632px">Address Line 1*</label>
    <div class="abs field" style="top:654px"></div>
    <label class="abs field-label" style="top:719px">Address Line 2*</label>
    <div class="abs field" style="top:741px"></div>
    <label class="abs field-label" style="top:806px">City</label>
    <label class="abs field-label" style="top:806px;left:199px">State</label>
    <div class="abs field" style="top:828px;width:168px"></div>
    <div class="abs field" style="top:828px;left:199px;width:168px"></div>
  </section>

  <!-- Contact detail -->
  <section class="screen screen--detail">
    <div class="abs status-time">9:41</div>
    <div class="abs island"></div>
    <svg class="abs status-icons" width="62" height="12" viewBox="0 0 62 12"><rect x="0" y="8" width="3" height="4" fill="#111"/><rect x="4" y="6" width="3" height="6" fill="#111"/><rect x="8" y="4" width="3" height="8" fill="#111"/><rect x="12" y="1" width="3" height="11" fill="#111"/><path d="M22 5a9 9 0 0 1 12 0M24.5 7.5a5 5 0 0 1 7 0" stroke="#111" stroke-width="1.8" fill="none"/><circle cx="28" cy="10.5" r="1.4" fill="#111"/><rect x="39" y="1" width="21" height="10" rx="3" fill="none" stroke="#111"/><rect x="41" y="3" width="17" height="6" rx="1.5" fill="#111"/></svg>
    <svg class="abs back" width="20" height="18" viewBox="0 0 20 18" fill="none" stroke="#111" stroke-width="2" stroke-linecap="round" stroke-linejoin="round"><path d="M18 9H2M9 2L2 9l7 7"/></svg>
    <h1 class="abs title">Contact</h1>

    <div class="abs row" style="top:128px">Add Email<svg width="16" height="16" viewBox="0 0 16 16"><path d="M8 1v14M1 8h14" stroke="#333" stroke-width="1.6"/></svg></div>
    <div class="abs row" style="top:192px">Add Social Media<svg width="16" height="16" viewBox="0 0 16 16"><path d="M8 1v14M1 8h14" stroke="#333" stroke-width="1.6"/></svg></div>
    <div class="abs row" style="top:256px">Add Contact<svg width="16" height="16" viewBox="0 0 16 16"><path d="M8 1v14M1 8h14" stroke="#333" stroke-width="1.6"/></svg></div>
    <div class="abs row" style="top:320px">Add Work Info<svg width="16" height="16" viewBox="0 0 16 16"><path d="M8 1v14M1 8h14" stroke="#333" stroke-width="1.6"/></svg></div>
    <div class="abs row" style="top:384px">Add Personal Information<svg width="16" height="16" viewBox="0 0 16 16"><path d="M8 1v14M1 8h14" stroke="#333" stroke-width="1.6"/></svg></div>
    <div class="abs row" style="top:448px">Add Skills or Talent<svg width="16" height="16" viewBox="0 0 16 16"><path d="M8 1v14M1 8h14" stroke="#333" stroke-width="1.6"/></svg></div>
    <div class="abs row" style="top:512px">Add Resources<svg width="16" height="16" viewBox="0 0 16 16"><path d="M8 1v14M1 8h14" stroke="#333" stroke-width="1.6"/></svg></div>

    <div class="abs group">
      <div class="group-head">Aircraft Owner<svg width="16" height="10" viewBox="0 0 16 10" fill="none" stroke="#111" stroke-width="2" stroke-linecap="round" stroke-linejoin="round"><path d="M2 8l6-6 6 6"/></svg></div>
      <p class="group-line"><span style="margin-right:6px">Personal</span>Brennan Lowell</p>
      <p class="group-line"><b>Kestrel</b>K20</p>
    </div>

    <nav class="abs tabbar">
      <div class="tab-item tab-item--active"><svg width="22" height="22" viewBox="0 0 22 22" fill="none" stroke="currentColor" stroke-width="1.6"><circle cx="11" cy="7" r="3.5"/><path d="M4 19c0-4 3-6 7-6s7 2 7 6z" stroke-linejoin="round"/></svg>Contact</div>
      <div class="tab-item"><svg width="22" height="22" viewBox="0 0 22 22" fill="none" stroke="currentColor" stroke-width="1.6" stroke-linejoin="round"><path d="M11 3l7 4v8l-7 4-7-4V7z M4 7l7 4 7-4 M11 11v8"/></svg>Quote</div>
      <div class="tab-item"><svg width="22" height="22" viewBox="0 0 22 22" fill="none" stroke="currentColor" stroke-width="1.6"><rect x="3" y="7" width="16" height="12" rx="1.5"/><path d="M8 7V4h6v3M8 7v12M14 7v12"/></svg>Work Order</div>
      <div class="tab-item"><svg width="22" height="22" viewBox="0 0 22 22" fill="none" stroke="currentColor" stroke-width="1.6"><rect x="5" y="4" width="12" height="16" rx="1.5"/><rect x="8" y="2.5" width="6" height="3" rx="1"/></svg>Invoice</div>
      <div class="tab-item"><svg width="22" height="22" viewBox="0 0 22 22" fill="currentColor"><circle cx="5" cy="11" r="1.6"/><circle cx="11" cy="11" r="1.6"/><circle cx="17" cy="11" r="1.6"/></svg>More</div>
    </nav>
    <div class="abs home-bar"></div>
  </section>

</div>
</body>
</html>
```